Web Design Project for Quorvel Enterprises

Quorvel Enterprises is a small company with expertise in manufacturing, product development, global sourcing and retail. We provide sales/broker, import/export, private label and product development services to both manufacturers and retailers of food, beverage, health and beauty care and general merchandise. Would like a web site that incorporates images that inspire confidence in the areas of international trade and product development as well as convey the experience of founder and CEO in these areas.

Own web address quorvelenterprises.net and have hosting from brisk nest.com

Target Market(s)

Retail and manufacturing professionals.

Industry/Entity Type

It Company

Font styles to use
Serif
Sans Serif

Requirements
Must have
• Tabs for: Home, About Us, Services, Contact Us

```html
<!DOCTYPE html>
<html lang="en">
<head>
<meta charset="utf-8">
<title>Quorvel Enterprises</title>
<link href="https://fonts.googleapis.com/css2?family=Open+Sans:wght@400;600;700&family=Raleway:wght@400;500;600;700&display=swap" rel="stylesheet">
<style>
:root{
  --blue:#1d4e9e;
  --blue-dark:#153c7c;
  --blue-light:#2f6cc4;
  --ink:#2a2f36;
  --muted:#6b7178;
  --grey-bg:#e9ebee;
  --rule:#c9ced4;
  --white:#ffffff;
}
*{box-sizing:border-box;margin:0;padding:0}
html,body{width:1200px;height:2452px;overflow:hidden;background:var(--white)}
body{font-family:"Open Sans",sans-serif;color:var(--ink)}
.page{width:1200px;height:2452px;position:relative}
h2{font-family:"Raleway",sans-serif;font-weight:500;text-transform:uppercase}

/* header */
.masthead{height:104px;display:flex;align-items:center;padding-left:120px}
.brand{display:flex;align-items:center;gap:14px;font-family:"Raleway",sans-serif;font-weight:700;color:var(--blue);font-size:30px;letter-spacing:1px}
.brand-mark{width:34px;height:34px;background:var(--blue)}
.nav{height:44px;background:var(--blue);display:flex;padding-left:112px}
.nav a{color:var(--white);text-decoration:none;font-size:13px;font-weight:600;letter-spacing:.5px;padding:0 32px;line-height:44px;text-transform:uppercase}
.nav a.active{background:var(--blue-light)}

/* hero */
.hero{position:relative;height:492px}
.hero-art{position:absolute;inset:0;background:linear-gradient(160deg,#cfe2f6 0%,#8fb4de 35%,#3e6fa8 70%,#23456f 100%)}
.hero-caption{position:absolute;left:0;right:0;bottom:0;height:72px;background:rgba(15,25,40,.78);display:flex;align-items:center;justify-content:center;padding:0 230px;text-align:center;color:var(--white);font-family:"Raleway",sans-serif;font-size:17px;letter-spacing:.5px;line-height:1.4}
.hero-caption strong{color:#5fa0f0;font-weight:700}

/* services */
.services{height:228px;display:flex;justify-content:center;gap:70px;padding-top:30px}
.service{width:260px;text-align:center}
.service svg{width:46px;height:46px}
.service h3{font-family:"Raleway",sans-serif;font-size:16px;color:var(--blue);font-weight:700;margin:8px 0 10px;text-transform:uppercase}
.service p{font-size:11px;line-height:1.45;color:var(--muted)}

/* news */
.news{height:448px;background:var(--grey-bg);padding:40px 120px 0}
.news h2{font-size:34px;color:var(--ink)}
.news .rule{height:2px;background:var(--rule);margin:12px 0 14px}
.news .intro{font-size:12px;color:var(--muted);margin-bottom:22px}
.news .intro a{color:#2a9a3c;text-decoration:none}
.news-grid{display:flex;gap:24px}
.news-card{width:304px}
.news-photo{height:140px;margin-bottom:10px}
.news-card h3{font-family:"Raleway",sans-serif;font-size:17px;font-weight:700;line-height:1.25;margin-bottom:6px}
.news-card p{font-size:11px;line-height:1.45;color:var(--muted)}

/* reviews */
.reviews{height:352px;padding:48px 120px 0;position:relative}
.reviews h2{font-size:34px;color:var(--ink)}
.reviews .rule{height:2px;background:var(--rule);margin:12px 0 22px}
.quote{display:flex;gap:30px}
.quote svg{width:74px;height:60px;flex:none}
.quote-body{flex:1}
.quote-body p{font-size:13px;line-height:1.6;color:var(--muted)}
.quote-author{font-style:normal;font-weight:700;font-size:14px;color:var(--ink);margin-top:16px}
.dots{display:flex;gap:9px;margin-top:20px}
.dots span{width:10px;height:10px;border-radius:50%;background:#9aa3ad}
.dots span.on{background:var(--blue)}

/* columns */
.columns{height:488px;background:var(--grey-bg);display:flex;gap:36px;padding:40px 120px 0}
.col{width:296px}
.col h2{font-size:24px;text-transform:none;color:var(--ink);margin-bottom:8px}
.col .rule{height:2px;background:var(--rule);margin-bottom:16px}
.col p{font-size:12px;line-height:1.5;color:var(--muted);margin-bottom:12px}
.btn{display:inline-block;background:var(--blue);color:var(--white);font-size:11px;font-weight:700;padding:12px 22px;text-transform:uppercase}
.media{display:flex;gap:12px;margin-bottom:12px}
.media-photo{width:138px;height:118px;flex:none;background:linear-gradient(160deg,#dfe4ea,#7d8896)}
.media p{margin:0}

/* newsletter */
.newsletter{height:200px;background:var(--blue);color:var(--white);text-align:center;padding-top:44px}
.newsletter h2{font-size:24px;font-weight:700;letter-spacing:1px}
.newsletter p{font-size:12px;margin:8px 0 18px;opacity:.9}
.subscribe{display:inline-flex}
.subscribe span{width:210px;height:30px;background:var(--white);color:var(--muted);font-size:11px;text-align:left;padding:7px 10px}
.subscribe b{width:64px;height:30px;background:var(--blue-light);font-size:11px;line-height:30px;font-weight:600}

/* footer */
.footer{height:92px;display:flex;align-items:center;justify-content:space-between;padding:0 120px}
.footer .brand{font-size:24px}
.footer .brand-mark{width:26px;height:26px}
.footer-mid{text-align:center;font-size:11px;color:var(--muted)}
.social{display:flex;gap:8px;justify-content:center;margin-bottom:6px}
.social span{width:16px;height:16px;border-radius:50%;background:var(--blue)}
.footer-addr{font-size:11px;color:var(--muted);line-height:1.5;display:flex;gap:10px}
.footer-addr strong{color:var(--ink)}
</style>
</head>
<body>
<div class="page">
  <header>
    <div class="masthead">
      <div class="brand"><span class="brand-mark"></span>QUORVEL ENTERPRISES</div>
    </div>
    <nav class="nav">
      <a class="active" href="#">Home</a><a href="#">About Us</a><a href="#">Services</a><a href="#">Latest News</a><a href="#">Testimonials</a><a href="#">Contact Us</a>
    </nav>
  </header>

  <section class="hero">
    <div class="hero-art" role="img" aria-label="Businessman with arms open in front of glass skyscrapers under a blue sky"></div>
    <div class="hero-caption"><p><strong>QUORVEL ENTERPRISES</strong> IS A SMALL COMPANY WITH EXPERTISE IN MANUFACTURING, PRODUCT DEVELOPMENT, GLOBAL SOURCING AND RETAIL.</p></div>
  </section>

  <section class="services">
    <div class="service">
      <svg viewBox="0 0 46 46" fill="none" stroke="#1d4e9e" stroke-width="3"><circle cx="20" cy="20" r="12"/><path d="M29 29l12 12"/></svg>
      <h3>Product Development</h3>
      <p>Sed ut perspiciatis, unde omnis iste natus error sit voluptatem accusantium doloremque laudantium totam rem aperiam.</p>
    </div>
    <div class="service">
      <svg viewBox="0 0 46 46" fill="#1d4e9e"><circle cx="23" cy="13" r="9"/><path d="M6 44c0-11 8-18 17-18s17 7 17 18z"/></svg>
      <h3>Sales/Broker</h3>
      <p>Quis autem vel eum iure reprehenderit qui in ea voluptate velit esse quam nihil molestiae consequatur vel illum.</p>
    </div>
    <div class="service">
      <svg viewBox="0 0 46 46" fill="#1d4e9e"><circle cx="14" cy="14" r="7"/><circle cx="32" cy="14" r="7"/><path d="M1 40c0-9 6-15 13-15s13 6 13 15zM19 40c0-9 6-15 13-15s13 6 13 15z"/></svg>
      <h3>Import/Export</h3>
      <p>Sed ut perspiciatis, unde omnis iste natus error sit voluptatem accusantium doloremque laudantium totam rem.</p>
    </div>
  </section>

  <section class="news">
    <h2>Latest News</h2>
    <div class="rule"></div>
    <p class="intro">To read the latest news, please <a href="#">register here</a> or if already a member <a href="#">sign in</a>.</p>
    <div class="news-grid">
      <article class="news-card">
        <div class="news-photo" role="img" aria-label="Banknotes spread out" style="background:linear-gradient(135deg,#c9d79a,#6f9a5a)"></div>
        <h3>Australian dollar continues range-trading</h3>
        <p>Harlow Diagnostics, the cancer testing company, rose on firm trading, as investors weighed prospects for growth in the year ahead and steady demand.</p>
      </article>
      <article class="news-card">
        <div class="news-photo" role="img" aria-label="City skyline with a tall tower" style="background:linear-gradient(160deg,#8a9098,#3c4148)"></div>
        <h3>NZ shares slump to four-month low in global sell-off</h3>
        <p>New Zealand stocks joined a global sell-off as rising geopolitical tensions and soft world markets weighed on investors’ appetite for risk.</p>
      </article>
      <article class="news-card">
        <div class="news-photo" role="img" aria-label="Bank branch sign on a street" style="background:linear-gradient(135deg,#2b2f35,#e0b72a)"></div>
        <h3>Five things to watch when TBK delivers earnings</h3>
        <p>The lender has signalled that full-year profit will climb, and markets expect a rise in the final dividend for the next few years.</p>
      </article>
    </div>
  </section>

  <section class="reviews">
    <h2>Customer Reviews</h2>
    <div class="rule"></div>
    <div class="quote">
      <svg viewBox="0 0 74 60" fill="#d5d9de"><path d="M0 60V34C0 14 10 3 28 0l3 7C20 11 15 18 15 28h14v32zM42 60V34C42 14 52 3 70 0l3 7C62 11 57 18 57 28h14v32z"/></svg>
      <div class="quote-body">
        <p>Sed ut perspiciatis, unde omnis iste natus error sit voluptatem accusantium doloremque laudantium, totam rem aperiam eaque ipsa, quae ab illo inventore veritatis et quasi architecto beatae vitae dicta sunt, explicabo. Nemo enim ipsam voluptatem, quia voluptas sit, aspernatur aut odit aut fugit, sed quia consequuntur magni dolores eos, qui ratione voluptatem sequi nesciunt, neque porro quisquam est, qui dolorem ipsum, quia dolor sit amet consectetur adipisci velit, sed quia non numquam eius modi tempora incidunt, ut labore et dolore magnam aliquam quaerat voluptatem.</p>
        <div class="quote-author">Director, Veltra Capital</div>
        <div class="dots"><span class="on"></span><span></span><span></span><span></span></div>
      </div>
    </div>
  </section>

  <section class="columns">
    <div class="col">
      <h2>Who Choose Us</h2>
      <div class="rule"></div>
      <p>Lorem ipsum dolor sit amet, consectetur adipiscing elit, sed do eiusmod tempor incididunt ut labore et dolore magna aliqua.</p>
      <p>Ut enim ad minim veniam, quis nostrud exercitation ullamco laboris nisi ut aliquip ex ea commodo consequat. Duis aute irure dolor in reprehenderit in voluptate velit esse cillum dolore eu fugiat nulla pariatur.</p>
      <span class="btn">Read more</span>
    </div>
    <div class="col">
      <h2>Our Experience</h2>
      <div class="rule"></div>
      <div class="media">
        <div class="media-photo" role="img" aria-label="Team of business people in suits"></div>
        <p>Our group is a joint venture of 5 independent companies. Each firm acts as a stand-alone unit within the group.</p>
      </div>
      <p>Ut enim ad minim veniam, quis nostrud exercitation ullamco laboris nisi ut aliquip ex ea commodo consequat. Duis aute irure dolor in reprehenderit in voluptate velit esse cillum dolore eu fugiat nulla pariatur.</p>
    </div>
    <div class="col">
      <h2>About Quorvel</h2>
      <div class="rule"></div>
      <div class="media">
        <div class="media-photo" role="img" aria-label="Business partners meeting in an office"></div>
        <p>Lorem ipsum dolor sit amet, consectetur adipiscing elit, sed do eiusmod tempor incididunt ut labore et dolore magna aliqua.</p>
      </div>
      <p>Ut enim ad minim veniam, quis nostrud exercitation ullamco laboris nisi ut aliquip ex ea commodo consequat. Duis aute irure dolor in reprehenderit in voluptate velit esse cillum dolore eu fugiat nulla pariatur.</p>
    </div>
  </section>

  <section class="newsletter">
    <h2>Subscribe to Newsletter</h2>
    <p>Lorem ipsum dolor sit amet, consectetur adipiscing elit, sed do eiusmod tempor incididunt ut labore.</p>
    <div class="subscribe"><span>your email</span><b>Submit</b></div>
  </section>

  <footer class="footer">
    <div class="brand"><span class="brand-mark"></span>QUORVEL ENTERPRISES</div>
    <div class="footer-mid">
      <div class="social"><span></span><span></span><span></span></div>
      Copyright © 2014 | Terms | Privacy
    </div>
    <div class="footer-addr">
      <svg width="14" height="18" viewBox="0 0 14 18" fill="#1d4e9e"><path d="M7 0a7 7 0 0 0-7 7c0 5 7 11 7 11s7-6 7-11a7 7 0 0 0-7-7zm0 10a3 3 0 1 1 0-6 3 3 0 0 1 0 6z"/></svg>
      <div>9870 Marrow Lane,<br>EASTFORD, DC 45 FR 45<br><strong>CALL US: 1 800 555 0134</strong></div>
    </div>
  </footer>
</div>
</body>
</html>
```